PROFESSIONAL MODERN REDESIGN OF CURRENT WEBSITE USING ALL SAME CONTENT

I need to redesign existing website using all existing exact content. Please do not leave anything missing. Use all content.

www.brightlanepromoworks.biz

Target Market(s)

Small business owners, business to business, B2B

Industry/Entity Type

Direct Marketing

Number of Pages Required

5+ page

Colors

Designer to choose colors to be used in the design.

Requirements
Must have
• Must use exact same content as www.brightlanepromoworks.biz
Nice to have
• I'd like this to be an easy to read professionally designed website with all modern elements...
Should not have
• Open

```html
<!DOCTYPE html>
<html lang="en">
<head>
<meta charset="utf-8">
<title>Brightlane Promoworks – Premium Incentive Marketing Services</title>
<link href="https://fonts.googleapis.com/css2?family=Dosis:wght@500;600;700&family=Raleway:wght@400;500;600&display=swap" rel="stylesheet">
<style>
:root{
  --orange:#f7941d;
  --orange-soft:#fde9cf;
  --blue:#1573c6;
  --blue-deep:#0f5fae;
  --blue-band:#1775c9;
  --navy:#0b1428;
  --ink:#222831;
  --muted:#555c66;
  --light:#f3f4f7;
  --white:#ffffff;
}
*{box-sizing:border-box;margin:0;padding:0}
html,body{width:1200px;height:3417px;overflow:hidden}
body{position:relative;background:var(--white);font-family:"Raleway",sans-serif;color:var(--ink)}
.abs{position:absolute}
.heading{font-family:"Dosis",sans-serif;font-weight:600;color:var(--orange);text-align:center}
.btn{position:absolute;display:flex;align-items:center;justify-content:center;border-radius:30px;background:var(--blue);color:var(--white);font-family:"Dosis",sans-serif;font-weight:600;font-size:14px;box-shadow:0 6px 14px rgba(21,115,198,.35)}
.hex{position:absolute;background:var(--orange-soft);clip-path:polygon(25% 5%,75% 5%,100% 50%,75% 95%,25% 95%,0 50%)}

/* header */
.brand{left:85px;top:30px;display:flex;align-items:center;gap:10px;font-family:"Dosis",sans-serif;font-weight:700;font-size:24px;color:var(--blue)}
.brand-mark{width:34px;height:34px;background:var(--blue)}
.top-links{left:733px;top:16px;font-size:14px;color:#6a9bd6;display:flex;gap:32px}
.phone{left:892px;top:8px;width:36px;height:36px;border-radius:50%;background:var(--blue)}
.office{left:943px;top:12px;font-size:10.5px;line-height:15px;color:var(--ink)}
.rule{left:727px;top:53px;width:387px;height:1px;background:#c9ccd2}
.nav{right:86px;top:68px;display:flex;gap:34px;font-size:14px;font-weight:500}
.nav .active{color:var(--blue)}

/* hero */
.hero-title{left:88px;top:252px;font-family:"Dosis",sans-serif;font-weight:700;font-size:35px;line-height:42px;color:var(--orange)}
.hero-sub{left:86px;top:350px;width:430px;font-family:"Dosis",sans-serif;font-weight:500;font-size:16.5px;line-height:26px;color:var(--ink)}
.watch{left:318px;top:463px;display:flex;align-items:center;gap:10px;font-family:"Dosis",sans-serif;font-weight:600;font-size:14px}
.play{width:34px;height:34px;border-radius:50%;border:2px solid var(--orange);display:flex;align-items:center;justify-content:center}

/* right fit */
.sub{font-size:12.5px;color:var(--muted);text-align:center}
.fit{top:775px;width:170px;margin-left:-85px;text-align:center;font-family:"Dosis",sans-serif;font-weight:500;font-size:16px;line-height:21px;color:var(--ink)}
.fit svg{display:block;margin:0 auto 12px}

/* cards */
.card{position:absolute;width:240px;border-top:3px solid var(--blue)}
.card.o{border-top-color:var(--orange)}
.card .img{height:116px}
.card .label{height:53px;background:var(--blue);color:var(--white);font-family:"Dosis",sans-serif;font-weight:600;font-size:15px;display:flex;align-items:center;justify-content:center;text-align:center}
.card-text{position:absolute;width:240px;text-align:center;font-size:11.5px;line-height:20px;color:#333}
.card-text b{color:var(--blue);font-weight:600}
.view{position:absolute;font-family:"Dosis",sans-serif;font-weight:600;font-size:13.5px;color:var(--blue);display:flex;align-items:center;gap:20px}

/* plug */
.plug{position:absolute;width:335px;height:128px;background:var(--white);display:flex;box-shadow:0 4px 14px rgba(0,0,0,.08)}
.plug .img{width:129px;flex:none}
.plug .txt{padding:9px 8px}
.plug h4{font-family:"Dosis",sans-serif;font-weight:500;font-size:14px;line-height:18px;margin-bottom:5px}
.plug p{font-size:10px;line-height:17px;color:#666}

/* band */
.band{left:0;top:2131px;width:1200px;height:497px;background:var(--blue-band)}
.dist{position:absolute;top:2250px;width:240px;margin-left:-120px;text-align:center;color:var(--white)}
.dist .ring{width:100px;height:100px;margin:0 auto;border-radius:50%;background:var(--white);border:5px solid var(--orange);display:flex;align-items:center;justify-content:center}
.dist h3{margin-top:20px;font-family:"Dosis",sans-serif;font-weight:600;font-size:19px}
.dist p{margin-top:12px;font-size:12px;line-height:19px}

/* promo */
.promo-bg{left:0;top:2628px;width:1200px;height:789px;background:linear-gradient(#f2f2f4,#fafafa)}
.promo .label{height:50px;font-size:19px}

.offer{left:227px;top:3098px;width:274px;height:292px;background:linear-gradient(160deg,#1c86e0,#0f6cc1);color:var(--white);text-align:center;padding:0 12px}
.offer h4{font-family:"Dosis",sans-serif;font-weight:600;font-size:17px;color:#ffc233;padding:16px 0 22px}
.offer p{font-size:14px;font-weight:600;line-height:21px;padding:20px 0 18px;border-top:1px solid rgba(255,255,255,.35)}
.offer p:first-of-type{border-top:none;padding-top:10px}
.start{left:568px;top:3103px;width:470px}
.start h3{font-family:"Dosis",sans-serif;font-weight:600;font-size:18px;margin-bottom:18px}
.start p{font-size:14px;line-height:22px;color:#5a5f66;margin-bottom:20px}
</style>
</head>
<body>

<!-- header -->
<div class="abs brand"><span class="brand-mark"></span>Brightlane Promoworks</div>
<div class="abs top-links"><span>Log In</span><span>Sign Up</span></div>
<div class="abs phone"><svg width="36" height="36" viewBox="0 0 36 36"><path d="M12 10c2 0 3 4 3 5s-2 2-1 4 3 4 5 5 3-1 4-1 5 1 5 3-2 4-4 4c-6 0-15-9-15-15 0-2 1-5 3-5z" fill="#fff"/></svg></div>
<div class="abs office">USA Office : 555-014-2278<br>International : 1-800-555-0163</div>
<div class="abs rule"></div>
<nav class="abs nav"><span>Home</span><span>Our Incentives</span><span>Samples</span><span>Affiliates</span><span>Testimonials</span><span>Faqs</span><span class="active">Contact</span></nav>

<!-- hero -->
<div class="hex" style="left:-10px;top:140px;width:66px;height:90px;background:#eef3fa"></div>
<div class="hex" style="left:486px;top:138px;width:86px;height:86px"></div>
<div class="hex" style="left:455px;top:540px;width:86px;height:86px;opacity:.7"></div>
<h1 class="abs hero-title">PREMIUM INCENTIVE<br>MARKETING SERVICES</h1>
<p class="abs hero-sub">Boost Sales From Your Existing Marketing Efforts Creating Exciting Promotions With Access To Unlimited Quantity of Our Incentive Certificates</p>
<div class="btn" style="left:86px;top:454px;width:206px;height:52px">Sign Up For Free 30 day Trial</div>
<div class="abs watch"><span class="play"><svg width="12" height="14"><path d="M1 1l10 6-10 6z" fill="var(--orange)"/></svg></span>Watch Video</div>
<svg class="abs" style="left:670px;top:102px" width="530" height="476" viewBox="0 0 530 476">
  <path d="M20 290 C40 380 120 440 230 470 C300 476 340 460 380 430 L150 330 Z" fill="var(--orange)"/>
  <path d="M0 0 H530 V388 C500 410 450 440 400 450 C300 450 200 420 120 370 C60 330 20 300 10 260 Z" fill="var(--navy)"/>
  <rect x="110" y="20" width="330" height="430" rx="120" fill="#2b2f3a" role="img" aria-label="Photo of a smiling businesswoman in a dark blazer with arms crossed"/>
  <circle cx="313" cy="256" r="23" fill="none" stroke="var(--orange)" stroke-width="3"/>
  <path d="M306 244l18 12-18 12z" fill="var(--orange)"/>
</svg>

<!-- right fit -->
<h2 class="abs heading" style="left:0;top:666px;width:1200px;font-size:29px">Right Fit And Logical Choice</h2>
<p class="abs sub" style="left:0;top:709px;width:1200px">See How We Are Better Than others</p>

<div class="abs fit" style="left:162px"><svg width="80" height="76"><polygon points="20,4 60,4 78,38 60,72 20,72 2,38" fill="var(--orange-soft)"/><rect x="30" y="10" width="36" height="50" fill="none" stroke="var(--blue)" stroke-width="3"/><circle cx="30" cy="44" r="8" fill="var(--blue)"/><path d="M16 68a14 12 0 0 1 28 0z" fill="var(--blue)"/><path d="M40 22h20M40 30h20M48 40h12" stroke="var(--blue)" stroke-width="3"/></svg>14+ Years In<br>Business</div>
<div class="abs fit" style="left:289px"><svg width="80" height="76"><polygon points="20,4 60,4 78,38 60,72 20,72 2,38" fill="var(--orange-soft)"/><circle cx="26" cy="18" r="7" fill="#f5b800"/><circle cx="54" cy="18" r="7" fill="#f5b800"/><circle cx="40" cy="14" r="7" fill="#f5b800"/><circle cx="22" cy="40" r="8" fill="var(--blue)"/><circle cx="40" cy="36" r="8" fill="var(--blue)"/><circle cx="58" cy="40" r="8" fill="var(--blue)"/><path d="M8 66a14 14 0 0 1 28 0zM26 62a14 14 0 0 1 28 0zM44 66a14 14 0 0 1 28 0z" fill="var(--blue)"/></svg>15,000+ Clients<br>Enrolled</div>
<div class="abs fit" style="left:451px"><svg width="80" height="76"><polygon points="20,4 60,4 78,38 60,72 20,72 2,38" fill="var(--orange-soft)"/><rect x="18" y="6" width="44" height="62" fill="#fff" stroke="var(--blue)" stroke-width="3"/><path d="M26 20h28M26 28h28" stroke="#f5b800" stroke-width="3"/><circle cx="40" cy="46" r="7" fill="none" stroke="var(--blue)" stroke-width="3"/><path d="M35 52l-2 12 7-4 7 4-2-12" fill="var(--blue)"/></svg>4+ Million Certificates<br>Distributed</div>
<div class="abs fit" style="left:642px"><svg width="80" height="76"><polygon points="20,4 60,4 78,38 60,72 20,72 2,38" fill="var(--orange-soft)"/><rect x="10" y="26" width="60" height="14" fill="none" stroke="var(--blue)" stroke-width="3"/><rect x="14" y="40" width="52" height="28" fill="none" stroke="var(--blue)" stroke-width="3"/><path d="M30 26v42M50 26v42" stroke="var(--blue)" stroke-width="3"/><path d="M40 26c-6-14-18-14-14-4zM40 26c6-14 18-14 14-4z" fill="none" stroke="#f5b800" stroke-width="3"/></svg>Hundreds Of Thousands<br>Of Redemptions</div>
<div class="abs fit" style="left:830px"><svg width="80" height="76"><polygon points="20,4 60,4 78,38 60,72 20,72 2,38" fill="var(--orange-soft)"/><circle cx="40" cy="24" r="9" fill="none" stroke="#f5b800" stroke-width="5" stroke-dasharray="4 3"/><circle cx="40" cy="24" r="4" fill="var(--blue)"/><path d="M8 52c10-6 20-6 30 0h14c4 0 4 6 0 6H36M8 62c10 6 30 8 52-8 6-4 10 0 6 4-18 16-40 18-58 12" fill="none" stroke="var(--blue)" stroke-width="3"/></svg>Top Notch Customer<br>Service</div>
<div class="abs fit" style="left:1008px"><svg width="80" height="76"><polygon points="20,4 60,4 78,38 60,72 20,72 2,38" fill="var(--orange-soft)"/><rect x="8" y="10" width="64" height="44" fill="#fff" stroke="var(--blue)" stroke-width="3"/><path d="M18 22h44M18 30h44" stroke="#f5b800" stroke-width="3"/><circle cx="40" cy="46" r="7" fill="none" stroke="var(--blue)" stroke-width="3"/><path d="M35 52l-2 14 7-4 7 4-2-14" fill="var(--blue)"/></svg>Licensed Seller Of<br>Travel CST #4410287</div>

<!-- unlimited -->
<div class="abs" style="left:0;top:977px;width:1200px;height:1154px;background:linear-gradient(#f4f5f8,#ffffff 35%,#f1f3f6 60%,#eef0f3)"></div>
<div class="abs" role="img" aria-label="Faint background photo of business people in a meeting" style="left:0;top:1560px;width:1200px;height:571px;background:linear-gradient(90deg,rgba(180,190,205,.35),rgba(255,255,255,.2) 50%,rgba(253,225,180,.45))"></div>
<h2 class="abs heading" style="left:0;top:1028px;width:1200px;font-size:29px">Unlimited Amount of Gift certificates</h2>
<p class="abs sub" style="left:0;top:1073px;width:1200px;font-size:11px;line-height:17px">For $99/Mo You CanAttract More Customers By Creating Sxciting Promotional<br>Giveaways Using an unimited amount of certificates redeemable for :</p>

<div class="card" style="left:93px;top:1167px"><div class="img" role="img" aria-label="Photo of an airliner flying through clouds" style="background:linear-gradient(#5f7d92,#a9bccb)"></div><div class="label">Vacation Getaway Certificates</div></div>
<div class="card o" style="left:350px;top:1167px"><div class="img" role="img" aria-label="Photo of plated restaurant food on a dark table" style="background:linear-gradient(135deg,#3a2e26,#b77a2e)"></div><div class="label">Restaurant Gift Certificates</div></div>
<div class="card" style="left:607px;top:1167px"><div class="img" role="img" aria-label="Photo of laptops, phones and gadgets on a desk" style="background:linear-gradient(135deg,#8b8f92,#cfd3d5)"></div><div class="label">Electronic Product Giveaways</div></div>
<div class="card o" style="left:864px;top:1167px"><div class="img" role="img" aria-label="Photo of a red neon wine sign" style="background:linear-gradient(90deg,#3a0508,#c41622,#3a0508)"></div><div class="label">Gas, Grocery &amp; Wine Vouchers</div></div>

<p class="card-text" style="left:93px;top:1350px">Resort Stays, Cruises &amp; Airfares<br>Up To <b>$3000.00</b> Retail Value Your<br>Customers Just Pay Taxes!</p>
<p class="card-text" style="left:350px;top:1350px"><b>$25-$300</b> Retail Value<br>Thousands Of Restaurants<br>Nationwide!</p>
<p class="card-text" style="left:607px;top:1350px">HD Tablets, Premium Earbuds,<br>Smart Watches, Mp4 Players<br><b>$100-$199</b> Retail Value</p>
<p class="card-text" style="left:864px;top:1350px">Available In <b>$50-$100</b><br>Denomination</p>

<div class="view" style="left:162px;top:1427px">View Certifications<svg width="24" height="10"><path d="M0 5h22M17 1l5 4-5 4" stroke="var(--blue)" fill="none" stroke-width="1.5"/></svg></div>
<div class="view" style="left:419px;top:1427px">View Certifications<svg width="24" height="10"><path d="M0 5h22M17 1l5 4-5 4" stroke="var(--blue)" fill="none" stroke-width="1.5"/></svg></div>
<div class="view" style="left:676px;top:1427px">View Certifications<svg width="24" height="10"><path d="M0 5h22M17 1l5 4-5 4" stroke="var(--blue)" fill="none" stroke-width="1.5"/></svg></div>
<div class="view" style="left:933px;top:1427px">View Certifications<svg width="24" height="10"><path d="M0 5h22M17 1l5 4-5 4" stroke="var(--blue)" fill="none" stroke-width="1.5"/></svg></div>

<div class="btn" style="left:497px;top:1484px;width:206px;height:50px">Get A 100% Free Sample Package</div>

<!-- plug -->
<h2 class="abs heading" style="left:0;top:1627px;width:1200px;font-size:29px">We Plug Right Into Your Existing advertising In 4 Major areas</h2>
<div class="plug" style="left:252px;top:1720px"><div class="img" role="img" aria-label="Photo of chess pieces on a board" style="background:linear-gradient(135deg,#2a3a55,#9aa8bd)"></div><div class="txt"><h4>Boost Response Rates To<br>Your Existing Ads</h4><p>Add a simple tagline to all your ads "Contact us today and receive Two Nights In Las Vegas, No Purchase Necessary!</p></div></div>
<div class="plug" style="left:613px;top:1720px"><div class="img" role="img" aria-label="Photo of business people shaking hands" style="background:linear-gradient(135deg,#2b2b2e,#8a8a8d)"></div><div class="txt"><h4>Get More New Customers</h4><p>Now that you have generated a new lead go ahead and offer a higher valued incentive like our Airfare Plus Hotel Getaway persuade them to purchase today vs tomorrow!</p></div></div>
<div class="plug" style="left:252px;top:1892px"><div class="img" role="img" aria-label="Photo of a rising bar chart graphic with a businessman" style="background:linear-gradient(135deg,#0c1a2e,#1f6f9e)"></div><div class="txt"><h4>Increase Repeat &amp;<br>Referral Business</h4><p>You have a reason to contact your clients to remind them about your services with a 7 Night Resort Getway to motivate them to buy again!</p></div></div>
<div class="plug" style="left:613px;top:1892px"><div class="img" role="img" aria-label="Photo of a hand touching a tablet showing charts" style="background:linear-gradient(135deg,#e6edf4,#9bbbd6)"></div><div class="txt"><h4>Boost Your Referral Business</h4><p>Offer a $100 Wine Voucher or even our Two Night Bahama Cruise to entice your customers to send you a referral and then watch your referral business soar!</p></div></div>

<div class="btn" style="left:497px;top:2061px;width:206px;height:50px">Quick 30 day Free trial Sign Up</div>

<!-- distribution -->
<div class="abs band"></div>
<h2 class="abs heading" style="left:0;top:2166px;width:1200px;font-size:29px">Easy Distribution of incentive</h2>
<svg class="abs" style="left:262px;top:2255px" width="680" height="110" fill="none" stroke="#f5c400" stroke-width="1.5" stroke-dasharray="3 4">
  <path d="M4 40l90 60M86 88l8 12-14-2"/><path d="M270 90l90-70M350 14l10 6-12 4"/><path d="M550 20l90 66M630 86l10 0-2-12"/>
</svg>
<div class="dist" style="left:190px"><div class="ring"><svg width="56" height="50" fill="none" stroke="var(--orange)" stroke-width="3"><rect x="14" y="2" width="28" height="14"/><rect x="3" y="16" width="50" height="20" rx="3"/><rect x="12" y="28" width="32" height="20" fill="#fff"/><path d="M18 36h20M18 42h14"/></svg></div><h3>Print</h3><p>Download PDF certificates to print and physically hand them out or mail them to your customers.</p></div>
<div class="dist" style="left:452px"><div class="ring"><svg width="56" height="44" fill="none" stroke="var(--orange)" stroke-width="3"><rect x="3" y="3" width="44" height="32"/><path d="M3 3l22 18L47 3"/><path d="M38 36h16M49 31l5 5-5 5"/></svg></div><h3>Email</h3><p>Email E-Certificates to your customers individually and in bulk with just one click.</p></div>
<div class="dist" style="left:731px"><div class="ring"><svg width="60" height="44" fill="none" stroke="var(--orange)" stroke-width="2.5"><rect x="3" y="8" width="46" height="18" rx="3"/><text x="9" y="21" font-size="9" fill="var(--orange)" stroke="none" font-family="Raleway,sans-serif">http://</text><path d="M40 18l12 22-6-2-3 6z" fill="#fff"/></svg></div><h3>Web Banners or API Integration</h3><p>Install our HTML web banners on the thank you pages of your website to automate distribution of our incentives and if you are tech savvy you can integrate our NEW API too!</p></div>
<div class="dist" style="left:1009px"><div class="ring"><svg width="56" height="50" fill="none" stroke="var(--orange)" stroke-width="3"><path d="M4 4h48v30H24l-10 12V34H4z"/><circle cx="18" cy="19" r="2.5" fill="var(--orange)"/><circle cx="28" cy="19" r="2.5" fill="var(--orange)"/><circle cx="38" cy="19" r="2.5" fill="var(--orange)"/></svg></div><h3>SMS/Text Messaging</h3><p>Send certificates through text messaging with just one click with our new SMS feature with no per sms fees!</p></div>
<div class="btn" style="left:497px;top:2551px;width:206px;height:52px;background:var(--white);color:var(--blue)">Click And we will&nbsp;<span style="color:var(--orange)">Call</span>&nbsp;You</div>

<!-- promo materials -->
<div class="abs promo-bg"></div>
<h2 class="abs heading" style="left:0;top:2680px;width:1200px;font-size:29px;line-height:31px">Promotional Marketing Materials To Help You<br>Promote The Incentive To Your Customers</h2>
<div class="card promo" style="left:93px;top:2802px"><div class="img" role="img" aria-label="Poster preview showing a city skyline at night" style="background:linear-gradient(135deg,#3a1c40,#d87a2a)"></div><div class="label">Posters &amp; Flyers</div></div>
<div class="card promo o" style="left:350px;top:2802px"><div class="img" role="img" aria-label="Illustration of a video player on a screen" style="background:linear-gradient(135deg,#f2f2f2,#c81f2a 60%,#f2f2f2)"></div><div class="label">Web Videos</div></div>
<div class="card promo" style="left:607px;top:2802px"><div class="img" role="img" aria-label="Preview of a product description brochure page" style="background:linear-gradient(#2a4d82 0 18%,#e9edf3 18%)"></div><div class="label">Product Description Brochures</div></div>
<div class="card promo" style="left:864px;top:2802px"><div class="img" role="img" aria-label="Preview of a marketing tips document page" style="background:linear-gradient(#2a4d82 0 24%,#f4f6f9 24%)"></div><div class="label">Tips</div></div>

<div class="abs offer">
  <h4>Get Promotional Design Material</h4>
  <p>You will get Professionally designed Flayers &amp; Posters</p>
  <p>You will also Get Professioanl Marketing Tips</p>
  <p>and Much More...</p>
</div>
<div class="abs start">
  <h3>Start Today</h3>
  <p>We help you by providing full color, professionally designed flyers &amp; posters for each incentive that you can get printed at your local print shop or any online printing company.</p>
  <p>We also provide you with customer appreciation letter templates and warm lead letter templates as well as proven incentive marketing tips and strategies to help you get the most from promotional campaigns.</p>
</div>
<div class="btn" style="left:562px;top:3333px;width:206px;height:50px;background:var(--blue-deep)">Contact Us Direct Today</div>

</body>
</html>
```